Offer banner redesign / Simplifying existing banner

We have a banner there customer can click on to get an offer. We want to simplify this banner and to get it to at minimum. We are not clear about how it shoulderstand look like, but the actual banner you can see here (It's at the top of the page): https://ofenrohr-lagerhaus.de/kaminsysteme/ We want to get rid of the icons and to reduce the size of the baner. The baner shoulderstand contain the Following text: Affordable chimney using installation service button text: Request free quote

Target Market(s)

Customers from age of 40yrs.

Requirements
Must have
• Clear and good visible button
Nice to have
• It Should be simple and striking.

```html
<!DOCTYPE html>
<html lang="de">
<head>
<meta charset="utf-8">
<title>Preiswerter Schornstein – Angebot anfordern</title>
<link rel="stylesheet" href="https://fonts.googleapis.com/css2?family=Montserrat:wght@700&family=Arimo:wght@400&display=swap">
<style>
  :root {
    --bg-light: #f4f4f4;
    --bg-mid: #ebebeb;
    --frame: #a9a9a9;
    --ink-dark: #3a3a3a;
    --ink-soft: #555555;
    --accent: #f8b133;
    --white: #ffffff;
  }
  html, body {
    margin: 0;
    padding: 0;
    overflow: hidden;
  }
  .offer-banner {
    position: relative;
    width: 1200px;
    height: 211px;
    overflow: hidden;
    background: linear-gradient(115deg, var(--bg-mid) 0%, var(--bg-light) 35%, var(--bg-mid) 60%, var(--bg-light) 100%);
  }
  .offer-banner__texture {
    position: absolute;
    inset: 0;
  }
  .offer-banner__headline-box {
    position: absolute;
    left: 50px;
    top: 28px;
    width: 661px;
    height: 156px;
    border: 1.5px solid var(--frame);
    display: flex;
    flex-direction: column;
    align-items: center;
    justify-content: center;
    box-sizing: border-box;
    padding-top: 2px;
  }
  .offer-banner__title {
    margin: 0;
    font-family: "Montserrat", sans-serif;
    font-weight: 700;
    font-size: 38.5px;
    line-height: 1;
    letter-spacing: 0;
    color: var(--ink-dark);
    white-space: nowrap;
  }
  .offer-banner__title-accent {
    color: var(--accent);
  }
  .offer-banner__subtitle {
    margin: 4px 0 0;
    font-family: "Arimo", Arial, sans-serif;
    font-weight: 400;
    font-size: 25.5px;
    line-height: 1.1;
    color: var(--ink-soft);
    white-space: nowrap;
  }
  .offer-banner__cta {
    position: absolute;
    left: 775px;
    top: 70px;
    width: 377px;
    height: 70px;
    border-radius: 35px;
    background: var(--accent);
    color: var(--white);
    font-family: "Montserrat", sans-serif;
    font-weight: 700;
    font-size: 19.5px;
    letter-spacing: 0.3px;
    text-decoration: none;
    white-space: nowrap;
    display: flex;
    align-items: center;
    justify-content: center;
  }
</style>
</head>
<body>
  <section class="offer-banner">
    <div class="offer-banner__texture" role="img" aria-label="Dezenter hellgrauer Hintergrund mit feinen geometrischen Flächen"></div>
    <div class="offer-banner__headline-box">
      <h1 class="offer-banner__title">PREISWERTER <span class="offer-banner__title-accent">SCHORNSTEIN</span></h1>
      <p class="offer-banner__subtitle">Wahlweise mit Montageservice</p>
    </div>
    <a class="offer-banner__cta" href="#angebot">kostenloses Angebot anfordern</a>
  </section>
</body>
</html>
```